Famous Australian Web Brand (SiteKeyHub.com.au) Needs a New Website & Logo

SiteKeyHub.com.au is one of the leading domain name registration businesses in Australia and is looking for an overhaul of its website and brand.

SiteKeyHub.com.au current products/services include domain name registration, web hosting, web site creation and SSL certificates.

In this design contest on PixelSwarm, we would like designers to create a new logo and new website design for SiteKeyHub.com.au.

Here is what contest entrants will need to create:
- 1 new logo
- 1 new home page design
- 1 internal page (pricing page)

The winning designer will receive the main prize of $750. In addition to this, the winning designer will have the opportunity to work with SiteKeyHub for the build of the full website and may get ongoing design work from SiteKeyHub.
Updates

thank you all for your designs, we are after a web 2.0 look and feel, please dont use serif fonts, lets use modern and sleek ones, i will upload some samples of one we like shortly

header is to be in black with some texturing, white fonts and the call to action buttons are in green.

for the 6 free services, please use round edges for the images with the text under it, as i will upload shortly and we would like custome images, not stockimage types please

im uploading a sample of a background image for the header, which is black with texturing and also and image for the footer/middle of the page which has the correct shading of the grey for the middle section

please see file 8 for the look we are trying to get with our site and for font ideas

Reason: we have decided to extend the contest for another 3 days as a couple of designers have requested a bit more time

Target Market(s)

People that might need to buy a domain name or start a website: small business owners; entrepreneurs; bloggers; everyone from mum-and-dad website owners to tech savvy entrepreneurs. Geographically we will be targeting Australia but this should not influence the design.

Industry/Entity Type

Build

Requirements
Must have
• The logo should:
- Have the text "SiteKeyHub"
- Be positioned in the top left hand corner of the website
- Be either a wordmark, pictorial or abstract logo. That is, text-only logos are acceptable but we are also interested in receiving logos with a mark to the left that could somehow represents the business that we’re in

The homepage should:
- Feel modern, slick, web2.0
- Have a horizontal menu with 4 menu items: About Us | Contact Us | My Cart | Login
- Include the logo at the top
- Include the content from this Word Document
- Include the rough layout and style from this JPG template layout

The interior page should:
- Have the same look and feel as the home page
- Include the rough layout and style from this JPG attachment
- Include the content from this second Word Document
Nice to have
• - Grey, white and black primary colors
- Buttons that are green or lime green with a web2.0 call to action
- Full-width design (i.e. across the screen like PixelSwarm)
Should not have
• - Do not include overt Australian references. While we are an Australian business we do not want Australian flags, kangaroos or Captain Bellwether in our logo or on our website.
- Do not use the current red color scheme in the design. We want to move away from this.

```html
<!DOCTYPE html>
<html lang="en">
<head>
<meta charset="utf-8">
<title>SiteKeyHub.com.au — Home</title>
<link rel="stylesheet" href="https://fonts.googleapis.com/css2?family=Open+Sans:ital,wght@0,400;0,600;0,700;1,400&display=swap">
<style>
  :root {
    --header-black: #000000;
    --nav-dark: #2a2a2a;
    --nav-mid: #3d3d3d;
    --nav-text: #b9b9b9;
    --white: #ffffff;
    --strip-grey: #e6e6e6;
    --page-grey: #f1f1f1;
    --card-white: #f7f7f7;
    --heading: #333333;
    --body-text: #8a8a8a;
    --promo-green: #eef2e2;
    --promo-border: #d6dcc6;
    --accent-green: #8db33a;
    --video-tone-a: #e9e1cf;
    --video-tone-b: #c98f6a;
  }
  * { margin: 0; padding: 0; box-sizing: border-box; }
  html, body { width: 1200px; height: 900px; overflow: hidden; }
  body {
    position: relative;
    background: var(--page-grey);
    font-family: "Open Sans", Arial, sans-serif;
  }
  .site-header {
    position: absolute; left: 0; top: 0; width: 1200px; height: 242px;
    background: var(--header-black);
  }
  .brand {
    position: absolute; left: 193px; top: 92px;
    display: flex; align-items: center; gap: 26px;
  }
  .brand-square {
    width: 82px; height: 82px; border-radius: 6px;
    background: var(--accent-green);
  }
  .brand-name {
    color: var(--white); font-weight: 700;
    font-size: 40px; letter-spacing: 9px; line-height: 1;
  }
  .main-nav {
    position: absolute; left: 0; top: 242px; width: 1200px; height: 54px;
    background: linear-gradient(180deg, var(--nav-mid), var(--nav-dark));
    border-bottom: 3px solid #cfcfcf;
  }
  .main-nav ul {
    list-style: none; position: absolute; left: 196px; top: 14px;
    display: flex; gap: 36px;
  }
  .main-nav li { color: var(--nav-text); font-size: 14px; letter-spacing: 0.5px; }
  .video-strip {
    position: absolute; left: 0; top: 308px; width: 1200px; height: 157px;
    background: var(--strip-grey);
    border-top: 1px solid #d4d4d4; border-bottom: 1px solid #d9d9d9;
  }
  .video-card {
    position: absolute; top: 36px; height: 84px;
    background: var(--card-white);
    display: flex; align-items: center;
  }
  .video-thumb {
    width: 119px; height: 77px; margin-left: 4px;
    border: 3px solid var(--white);
    box-shadow: 0 0 0 1px #cfcfcf;
    background: linear-gradient(90deg, var(--video-tone-a), var(--video-tone-b));
  }
  .video-title {
    margin-left: 10px; margin-top: 24px;
    font-size: 14px; line-height: 18px; color: #444;
  }
  .video-title.small { font-size: 11px; font-weight: 700; line-height: 14px; margin-top: 16px; }
  .promo-box {
    position: absolute; left: 186px; top: 496px; width: 889px; height: 98px;
    background: var(--promo-green);
    border: 1px solid var(--promo-border); border-radius: 4px;
  }
  .promo-text {
    position: absolute; left: 211px; top: 4px; width: 397px;
    background: var(--white); padding: 6px 4px;
    font-style: italic; font-size: 17px; line-height: 37px; color: #333;
    text-align: center;
  }
  .feature {
    position: absolute; top: 628px; width: 252px;
  }
  .feature-image {
    width: 251px; height: 184px; border-radius: 6px;
  }
  .feature h2 {
    margin-top: 18px; font-size: 16px; font-weight: 600; color: var(--heading);
  }
  .feature p {
    margin-top: 10px; font-size: 11.5px; line-height: 21px; color: var(--body-text);
  }
</style>
</head>
<body>
  <header class="site-header">
    <div class="brand">
      <span class="brand-square"></span>
      <span class="brand-name">SiteKeyHub.com.au</span>
    </div>
  </header>

  <nav class="main-nav">
    <ul>
      <li>Blog.</li>
      <li>Design.</li>
      <li>Design.</li>
    </ul>
  </nav>

  <section class="video-strip">
    <div class="video-card" style="left:193px; width:249px;">
      <div class="video-thumb" role="img" aria-label="Video thumbnail of a presenter beside a play button"></div>
      <div class="video-title">Everyone needs<br>a domain</div>
    </div>
    <div class="video-card" style="left:507px; width:233px;">
      <div class="video-thumb" role="img" aria-label="Video thumbnail of a presenter beside a play button"></div>
      <div class="video-title">How you can<br>use a domain</div>
    </div>
    <div class="video-card" style="left:823px; width:233px;">
      <div class="video-thumb" role="img" aria-label="Video thumbnail of a presenter beside a play button"></div>
      <div class="video-title small">Why Choose<br>SiteKeyHub</div>
    </div>
  </section>

  <div class="promo-box">
    <p class="promo-text">Everything your business needs to be successful<br>online is included FREE with every domain name.</p>
  </div>

  <article class="feature" style="left:190px;">
    <div class="feature-image" role="img" aria-label="Collage of colourful social network app tiles with a large SOCIAL headline and a just released ribbon" style="background:linear-gradient(135deg,#3a4a5c,#6a3d6e 50%,#2f5a3a);"></div>
    <h2>Know Your Visitors</h2>
    <p>Learn where they're coming from, and what<br>keywords they're using to find you. Our powerful</p>
  </article>

  <article class="feature" style="left:505px;">
    <div class="feature-image" role="img" aria-label="Smartphone screen showing a blog comments app" style="background:linear-gradient(180deg,#3a3a3a,#1c1c1c 60%,#9a9a9a);"></div>
    <h2>Know Your Visitors</h2>
    <p>Learn where they're coming from, and what<br>keywords they're using to find you. Our powerful</p>
  </article>

  <article class="feature" style="left:820px;">
    <div class="feature-image" role="img" aria-label="Blogging platforms linked to a sync icon" style="background:linear-gradient(90deg,#f4f4f4 0%,#f4f4f4 57%,#1e1e1e 57%,#2e2e2e 100%);border:1px solid #d0d0d0;"></div>
    <h2>Know Your Visitors</h2>
    <p>Learn where they're coming from, and what<br>keywords they're using to find you. Our powerful</p>
  </article>
</body>
</html>
```